Dental-Specific Brochure for IT Services

We are creating a brochure for IT services for local dental practices. Highlights should include:
- no contract / we earn your business on a month to month basis
- affordable pricing
- fast response times
- 25+ local dental practices
- predictable fixed-rate billing
Text should include:
Why Dental Practices Choose MPAK?At MPAK, we specialize in providing reliable, affordable, and high-quality IT solutions tailored specifically for dental offices. With over 25 local dental practices trusting us with their IT needs, we understand the unique challenges you face and offer solutions to keep your practice running smoothly.
What Sets MPAK Apart?
✅ No Contracts – We believe in earning your business every month. Stay because you want to, not because you have to.
✅ Affordable Pricing – Cost-effective solutions that fit your budget without sacrificing quality.
✅ Fast Response Times – When you need IT support, we’re there. Minimize downtime and keep your practice operational.
✅ Predictable Fixed-Rate Billing – No surprises, just straightforward pricing that makes budgeting easy.
✅ Proven Track Record – Over 25 dental practices in the area trust MPAK for their IT support.
✅ Expert Cybersecurity & Ransomware Protection – Advanced security measures to protect patient data and experience with HIPAA HITECH Act.
✅ Full Support for Practice Management Software – We work with Lumera Dental, Harvolink, Molavo, and other leading platforms.
Our IT Services for Dental Practices:
VoIP Phone Solutions – Reliable communication for your front desk and patient calls.
Managed IT Support – Proactive monitoring, maintenance, and troubleshooting to prevent downtime.
Cloud Solutions – Secure, scalable storage and software solutions for your practice.
Network & Wi-Fi Optimization – Fast, secure, and reliable internet for your office.
High-Speed Fiber Internet – Ensure fast and reliable connectivity to keep your practice running smoothly.
Let’s Get Started!
Join the growing number of dental practices that trust MPAK for their IT needs. Contact us today to schedule a consultation and see how we can help your practice thrive.
-
We would like contact info displayed similarly to how it is on the other brochure in the attachments. I will also be adding some more pictures to use; feel free to add in holding spots for pictures similar to what is in the example brochure.
Logo is in attachments along with current brochure.

```html
<!DOCTYPE html>
<html lang="en">
<head>
<meta charset="utf-8">
<title>MPAK – IT Services for Dental Practices</title>
<link rel="stylesheet" href="https://fonts.googleapis.com/css2?family=Exo+2:wght@600;700;800&family=Lexend:wght@300;400;500;600;700&display=swap">
<style>
  :root{
    --royal:#1b2c9e;
    --navy:#101c78;
    --deep:#0b1460;
    --green:#8cc63f;
    --green-dark:#74ad2a;
    --ink:#1c1c2a;
    --white:#ffffff;
    --page:#ffffff;
  }
  *{box-sizing:border-box;margin:0;padding:0}
  html,body{width:1200px;height:1200px;overflow:hidden;background:var(--page)}
  body{font-family:"Lexend",sans-serif;color:var(--ink)}
  .flyer{position:absolute;left:136px;top:0;width:928px;height:1200px;background:var(--white);overflow:hidden}
  .abs{position:absolute}

  /* header */
  .hero{left:0;top:0;width:928px;height:366px;background:linear-gradient(135deg,var(--navy) 0%,var(--royal) 55%,#2236b8 100%)}
  .brand{left:68px;top:44px;font-family:"Exo 2",sans-serif;font-weight:700;font-size:78px;color:var(--white);letter-spacing:-1px;line-height:1}
  .headline{left:68px;top:150px;font-family:"Exo 2",sans-serif;font-weight:800;text-transform:uppercase;line-height:.9}
  .headline .l1{font-size:50px;color:var(--white);display:block}
  .headline .l2{font-size:50px;color:var(--green);display:block}
  .sub{left:68px;top:292px;text-transform:uppercase;line-height:1}
  .sub .s1{display:block;font-family:"Lexend",sans-serif;font-weight:400;font-size:20px;letter-spacing:4px;color:var(--white)}
  .sub .s2{display:block;font-family:"Exo 2",sans-serif;font-weight:700;font-size:31px;color:var(--green);margin-top:4px}
  .hero-photos{left:436px;top:40px;width:492px;height:340px;background:linear-gradient(160deg,#5b78d8 0%,#3a55c4 45%,#e9eef8 100%);clip-path:polygon(14% 0,100% 0,100% 100%,30% 100%,0 58%)}

  /* why */
  .why{left:67px;top:381px;width:808px;height:90px;border:1px solid #8a93c9;border-radius:8px}
  .why-tag{left:67px;top:381px;width:218px;height:90px;background:var(--green);border-radius:8px 0 0 8px;padding:12px 0 0 26px;font-family:"Exo 2",sans-serif;font-weight:700;font-size:22px;line-height:.9;color:var(--navy)}
  .why-tag b{color:var(--white);font-weight:700}
  .why-arrow{left:284px;top:411px;width:0;height:0;border-top:15px solid transparent;border-bottom:15px solid transparent;border-left:20px solid var(--green)}
  .why-text{left:333px;top:393px;width:522px;font-size:12.6px;line-height:1.33;color:var(--ink)}
  .why-text b{font-weight:600}

  /* features */
  .apart{left:81px;top:491px;font-family:"Exo 2",sans-serif;font-weight:800;font-size:26px;color:var(--navy);text-transform:uppercase}
  .feature{width:220px}
  .feature h3{font-family:"Exo 2",sans-serif;font-weight:700;font-size:15px;line-height:.85;color:var(--royal);text-transform:uppercase;margin-bottom:4px}
  .feature p{font-size:11.6px;line-height:1.28;color:var(--ink)}
  .icon{width:62px;height:62px;border-radius:50%;background:var(--green);border:4px solid var(--royal);box-shadow:inset 0 0 0 3px var(--white);display:flex;align-items:center;justify-content:center}
  .icon svg{width:30px;height:30px;fill:none;stroke:var(--white);stroke-width:1.8;stroke-linecap:round;stroke-linejoin:round}
  .clinic-photo{left:676px;top:483px;width:252px;height:382px;background:linear-gradient(180deg,#ffffff 0%,#e4ebf5 40%,#c9d5e8 75%,#ffffff 100%)}

  /* services */
  .services{left:51px;top:865px;width:833px;height:186px;border-radius:14px;background:linear-gradient(120deg,var(--deep) 0%,var(--royal) 55%,var(--deep) 100%);overflow:hidden}
  .services-bar{left:51px;top:865px;width:833px;height:36px;border-radius:14px 14px 0 0;background:var(--green)}
  .services-title{left:313px;top:869px;font-family:"Exo 2",sans-serif;font-weight:800;font-size:25px;color:var(--white);text-transform:uppercase;white-space:nowrap}
  .services-title span{color:var(--navy)}
  .phone-photo{left:82px;top:838px;width:150px;height:128px;border-radius:8px;background:linear-gradient(160deg,#5a6070 0%,#2b2f3a 60%,#9aa0ac 100%)}
  .service{width:250px}
  .service h4{font-family:"Exo 2",sans-serif;font-weight:700;font-size:15.5px;color:var(--green);text-transform:uppercase;display:flex;align-items:center;gap:5px;white-space:nowrap;margin-bottom:3px}
  .service h4 svg{width:13px;height:13px;flex:none}
  .service p{font-size:11.4px;line-height:1.3;color:var(--white);padding-left:19px}

  /* cta */
  .cta-tag{left:51px;top:1071px;width:106px;height:44px;background:var(--green);border-radius:5px;padding:7px 0 0 12px;font-family:"Exo 2",sans-serif;font-weight:700;font-size:15px;line-height:.85;color:var(--navy);text-transform:uppercase}
  .cta-arrow{left:156px;top:1085px;border-top:8px solid transparent;border-bottom:8px solid transparent;border-left:10px solid var(--green)}
  .cta-text{left:175px;top:1073px;width:720px}
  .cta-text strong{display:block;font-family:"Lexend",sans-serif;font-weight:700;font-size:13.6px;color:var(--royal);text-transform:uppercase;letter-spacing:-.3px}
  .cta-text span{display:block;font-size:13.2px;color:var(--ink);margin-top:2px}

  /* footer */
  .footer-green{left:0;top:1126px;width:928px;height:74px;background:var(--green)}
  .footer-blue{left:0;top:1126px;width:456px;height:74px;background:var(--royal);clip-path:polygon(0 0,100% 0,94% 100%,0 100%)}
  .call{left:48px;top:1147px;font-family:"Lexend",sans-serif;font-weight:700;font-size:25px;color:var(--white);white-space:nowrap;letter-spacing:.3px}
  .contact{left:471px;top:1148px;font-size:21px;color:var(--white);white-space:nowrap;display:flex;align-items:center;gap:16px}
  .contact .sep{width:2px;height:30px;background:var(--white)}
</style>
</head>
<body>
<main class="flyer">
  <header>
    <div class="abs hero"></div>
    <div class="abs hero-photos" role="img" aria-label="Collage of IT photos in diamond frames – server cables, cloud, support team, Wi-Fi, desk phone, fiber optics – beside a smiling dentist at a laptop"></div>
    <div class="abs brand">mpak</div>
    <h1 class="abs headline"><span class="l1">Unleash the</span><span class="l2">Power of</span><span class="l2">IT Services</span></h1>
    <p class="abs sub"><span class="s1">For your local</span><span class="s2">Dental Practices</span></p>
  </header>

  <section>
    <div class="abs why"></div>
    <h2 class="abs why-tag">Why Dental<br>Practices<br>Choose <b>MPAK?</b></h2>
    <div class="abs why-arrow"></div>
    <p class="abs why-text"><b>At MPAK</b>, we specialize in providing reliable, affordable, and high-quality IT solutions tailored specifically for dental offices. With over 25 local dental practices trusting us with their IT needs, we understand the unique challenges you face and offer solutions to keep your practice running smoothly.</p>
  </section>

  <section>
    <h2 class="abs apart">What sets MPAK apart?</h2>
    <div class="abs clinic-photo" role="img" aria-label="Dentist and assistant treating a patient in a bright modern dental clinic"></div>

    <div class="abs icon" style="left:66px;top:540px"><svg viewBox="0 0 30 30"><path d="M8 4h10l5 5v10M8 4v22h9"/><path d="M11 11h7M11 15h6"/><circle cx="22" cy="22" r="4"/><path d="M19 25l6-6"/></svg></div>
    <div class="abs feature" style="left:143px;top:546px"><h3>No Contracts</h3><p>We believe in earning your business every month. Stay because you want to, not because you have to.</p></div>

    <div class="abs icon" style="left:66px;top:616px"><svg viewBox="0 0 30 30"><circle cx="17" cy="9" r="5"/><path d="M17 7v4M4 22l5-4h6l4 2 7-5M4 26l4-2h10"/></svg></div>
    <div class="abs feature" style="left:143px;top:624px"><h3>Affordable Pricing</h3><p>Cost-effective solutions that fit your budget without sacrificing quality.</p></div>

    <div class="abs icon" style="left:66px;top:683px"><svg viewBox="0 0 30 30"><circle cx="16" cy="17" r="8"/><path d="M16 12v5l3 2M13 6h6M3 14h5M4 18h4M5 22h4"/></svg></div>
    <div class="abs feature" style="left:143px;top:690px"><h3>Fast Response Times</h3><p>When you need IT support, we’re there. Minimize downtime and keep your practice operational.</p></div>

    <div class="abs icon" style="left:66px;top:760px"><svg viewBox="0 0 30 30"><path d="M7 4h11l5 5v16H7z"/><path d="M10 18l7-7"/><circle cx="11" cy="12" r="1.5"/><circle cx="16" cy="17" r="1.5"/><rect x="18" y="20" width="7" height="6"/></svg></div>
    <div class="abs feature" style="left:143px;top:768px"><h3>Predictable Fixed-Rate Billing</h3><p>No surprises, just straightforward pricing that makes budgeting easy.</p></div>

    <div class="abs icon" style="left:383px;top:540px"><svg viewBox="0 0 30 30"><path d="M5 14h20l-2 11H7z"/><path d="M8 14V5h10l4 4v5"/><path d="M11 9h6M11 18h8"/></svg></div>
    <div class="abs feature" style="left:460px;top:546px"><h3>Proven Track Record</h3><p>Over 25 dental practices in the area trust MPAK for their IT support.</p></div>

    <div class="abs icon" style="left:383px;top:624px"><svg viewBox="0 0 30 30"><circle cx="15" cy="15" r="8"/><rect x="12" y="14" width="6" height="5"/><path d="M13 14v-2a2 2 0 014 0v2M15 3v4M15 23v4M3 15h4M23 15h4"/></svg></div>
    <div class="abs feature" style="left:460px;top:630px"><h3>Expert Cybersecurity &amp; Ransomware Protection</h3><p>Advanced security measures to protect patient data and experience with HIPAA HITECH Act.</p></div>

    <div class="abs icon" style="left:383px;top:735px"><svg viewBox="0 0 30 30"><rect x="6" y="5" width="13" height="21" rx="2"/><circle cx="12.5" cy="14" r="3"/><path d="M9 21c1-2 6-2 7 0M17 7h8v6h-6l-2 2"/></svg></div>
    <div class="abs feature" style="left:460px;top:741px"><h3>Full Support for Practice Management Software</h3><p>We work with Lumera Dental, Harvolink, Molavo, and other leading platforms.</p></div>
  </section>

  <section>
    <div class="abs services"></div>
    <div class="abs services-bar"></div>
    <h2 class="abs services-title">Our IT Services for <span>Dental Practices</span></h2>
    <div class="abs phone-photo" role="img" aria-label="Desk VoIP phone with color screen and handset"></div>

    <div class="abs service" style="left:314px;top:920px"><h4><svg viewBox="0 0 14 14"><circle cx="7" cy="7" r="6" fill="none" stroke="#fff" stroke-width="1.4"/><path d="M4 7l2 2 4-4" fill="none" stroke="#fff" stroke-width="1.4"/></svg>Managed IT Support</h4><p>Proactive monitoring, maintenance, &amp; troubleshooting to prevent downtime.</p></div>
    <div class="abs service" style="left:579px;top:920px"><h4><svg viewBox="0 0 14 14"><circle cx="7" cy="7" r="6" fill="none" stroke="#fff" stroke-width="1.4"/><path d="M4 7l2 2 4-4" fill="none" stroke="#fff" stroke-width="1.4"/></svg>High-Speed Fiber Internet</h4><p>Ensure fast and reliable connectivity to keep your practice running smoothly.</p></div>
    <div class="abs service" style="left:81px;top:987px"><h4><svg viewBox="0 0 14 14"><circle cx="7" cy="7" r="6" fill="none" stroke="#fff" stroke-width="1.4"/><path d="M4 7l2 2 4-4" fill="none" stroke="#fff" stroke-width="1.4"/></svg>VoIP Phone Solutions</h4><p style="padding-left:0">Reliable communication for your front desk and patient calls.</p></div>
    <div class="abs service" style="left:314px;top:987px"><h4><svg viewBox="0 0 14 14"><circle cx="7" cy="7" r="6" fill="none" stroke="#fff" stroke-width="1.4"/><path d="M4 7l2 2 4-4" fill="none" stroke="#fff" stroke-width="1.4"/></svg>Cloud Solutions</h4><p>Secure, scalable storage and software solutions for your practice.</p></div>
    <div class="abs service" style="left:579px;top:987px"><h4><svg viewBox="0 0 14 14"><circle cx="7" cy="7" r="6" fill="none" stroke="#fff" stroke-width="1.4"/><path d="M4 7l2 2 4-4" fill="none" stroke="#fff" stroke-width="1.4"/></svg>Network &amp; Wi-Fi Optimization</h4><p>Fast, secure, and reliable internet for your office.</p></div>
  </section>

  <section>
    <div class="abs cta-tag">Let’s get<br>started!</div>
    <div class="abs cta-arrow"></div>
    <p class="abs cta-text"><strong>Join the growing number of dental practices that trust MPAK for their IT needs.</strong><span>Contact us today to schedule a consultation and see how we can help your practice thrive.</span></p>
  </section>

  <footer>
    <div class="abs footer-green"></div>
    <div class="abs footer-blue"></div>
    <p class="abs call">CALL NOW&nbsp; 555-014-2287</p>
    <p class="abs contact"><span>sales@mpakit.com</span><span class="sep"></span><span>www.mpakit.com</span></p>
  </footer>
</main>
</body>
</html>
```